Wix Website design for my therapy business - Willowmere Group

I have started designing a Wix site and have a good idea of what I want.
I have set up the pages, created some design ideas, and inputted the copy. I need someone fabulous to finish off the design aspects. I like working closely with the designers, I was an interior designer in an old career.
I would like the site to be funky but professional. My Wix skills are limited, and I just can't achieve the look I am wanting without having to spend a lot of time learning. If it's easier to start over, that's ok providing you use the same colours, font, images etc. I have included a screenshot of the home page below. I have another site I need to start as soon as we have finished this one.
I am looking for someone who is a good listener and is has design flare. I am easy to get along with and will respond quickly.
I would like to set up SEO and have help in the future.
Let me know if you are the right person for the job.
Target Market(s)
Please needing help with their mental health and for therapy.
Industry/Entity Type
Mental health
Font styles to use
Other font styles liked:
- Futura light
Requirements
Must have
- be easy to navigate and be simple yet stylish
Nice to have
- I have set up the basics of the site - nice to haves are already on the site
Should not have
- old fashioned large chunks of text.

```html
<!DOCTYPE html>
<html lang="en">
<head>
<meta charset="utf-8">
<title>Willowmere Group – Therapy</title>
<link href="https://fonts.googleapis.com/css2?family=Ubuntu:wght@400;500;700&family=Poppins:wght@300;400;500;600&display=swap" rel="stylesheet">
<style>
:root{
  --brown:#9e8164;
  --brown-dark:#8b6f54;
  --band:#a68a6d;
  --beige:#f5eee8;
  --pale:#f6f8fb;
  --ink:#2b2b2b;
  --muted:#555;
  --white:#fff;
}
*{box-sizing:border-box;margin:0;padding:0}
html,body{width:1200px;height:4592px;overflow:hidden}
body{position:relative;background:var(--white);font-family:"Poppins",sans-serif;color:var(--ink)}
.abs{position:absolute}
section,header,footer{position:absolute;left:0;width:1200px;overflow:hidden}
.heading{font-family:"Ubuntu",sans-serif;font-weight:500;color:var(--brown);letter-spacing:.5px;white-space:nowrap}
.eyebrow{font-size:11px;font-weight:600;letter-spacing:.3px;color:#222;display:flex;align-items:center;gap:14px;text-transform:uppercase}
.eyebrow::after{content:"";width:50px;height:2px;background:#222}
.body-text{font-size:12.5px;line-height:24px;color:var(--muted)}
.btn{display:flex;align-items:center;justify-content:center;font-size:12px;font-weight:500;color:var(--white);background:var(--brown)}
.photo{position:absolute}
.arrow-btn{position:absolute;width:44px;height:62px;background:var(--white);box-shadow:0 2px 8px rgba(0,0,0,.12);display:flex;align-items:center;justify-content:center}

.top-bar{top:0;height:36px;background:var(--brown);color:var(--white);font-size:12px;display:flex;align-items:center;justify-content:center;gap:6px}
.site-header{top:36px;height:108px;background:var(--white)}
.brand{left:100px;top:26px;font-family:"Ubuntu",sans-serif;font-weight:500;font-size:28px;color:var(--brown);display:flex;align-items:center;gap:10px;line-height:1}
.brand-dot{width:14px;height:14px;border-radius:50%;background:var(--brown)}
.header-phone{left:688px;top:22px;font-size:17px;color:var(--brown);display:flex;align-items:center;gap:8px}
.header-cta{left:858px;top:14px;width:191px;height:40px;font-size:12px;letter-spacing:.3px}
.main-nav{left:423px;top:74px;display:flex;font-size:12px;font-weight:600;color:#222;white-space:nowrap}
.main-nav span{margin-right:25px}
.main-nav .active{color:var(--brown);border-bottom:2px solid var(--brown);padding-bottom:4px}

.hero{top:144px;height:691px}
.hero-photo{inset:0;background:linear-gradient(90deg,#5b7394 0%,#7a8fab 38%,#c9c3bf 62%,#e6ddd6 100%)}
.hero-tag{left:90px;top:196px;color:var(--white);font-size:13px;display:flex;align-items:center;gap:20px}
.hero-tag::after{content:"";width:46px;height:1px;background:var(--white)}
.hero-title{left:90px;top:226px;font-family:"Ubuntu",sans-serif;font-weight:500;font-size:43px;line-height:58px;color:var(--white);letter-spacing:1px;white-space:nowrap}
.hero-text{left:90px;top:403px;width:420px;font-size:12.5px;line-height:20px;color:#f1f1f1}
.hero-btn{left:90px;top:469px;width:192px;height:42px}

.conditions{top:835px;height:716px;background:var(--pale)}
.card{position:absolute;top:220px;width:321px;height:403px;background:var(--white);box-shadow:0 4px 14px rgba(0,0,0,.06);text-align:center}
.card .photo{left:0;top:0;width:321px;height:210px}
.card-icon{position:absolute;left:125px;top:175px;width:70px;height:70px;border-radius:50%;background:var(--brown);border:4px solid var(--white);display:flex;align-items:center;justify-content:center}
.card h3{position:absolute;top:264px;width:100%;font-family:"Ubuntu",sans-serif;font-weight:500;font-size:23px;color:var(--brown)}
.card p{position:absolute;top:305px;left:30px;width:261px;font-size:12.5px;line-height:24px;color:var(--muted)}
.card .rule{position:absolute;left:140px;top:372px;width:40px;height:2px;background:var(--brown)}

.why{top:1551px;height:642px;background:var(--white)}
.feature{position:absolute;width:260px}
.feature svg{position:absolute;left:0;top:0}
.feature h4{position:absolute;left:52px;top:0;font-size:15px;font-weight:500;color:var(--brown);white-space:nowrap}
.feature p{position:absolute;left:55px;top:28px;width:200px;font-size:12.5px;line-height:24px;color:var(--muted)}
.ring{left:642px;top:106px;width:468px;height:468px;border-radius:50%;border:10px solid var(--brown)}
.ring-photo{left:650px;top:132px;width:426px;height:426px;border-radius:50%;background:radial-gradient(circle at 60% 40%,#d8d2cb,#a49483 60%,#6f6257)}

.about{top:2193px;height:473px}
.about-panel{left:590px;top:43px;width:610px;height:401px;background:var(--beige)}
.about-frame{left:0;top:23px;width:590px;height:447px;border:5px solid var(--brown);background:linear-gradient(120deg,#e7e2dc,#cbbfb2 55%,#8f8172)}

.testimonials{top:2666px;height:633px;background:var(--white)}
.quote-card{position:absolute;top:224px;width:321px;height:242px;background:var(--beige);border-radius:26px;padding:40px 32px 0 31px}
.quote-mark{position:absolute;left:30px;top:-20px}
.stars{color:#f6b417;font-size:14px;letter-spacing:2px}
.quote-card h4{font-size:16px;font-weight:500;color:#222;margin:6px 0 6px}
.quote-card p{font-size:12px;line-height:24px;color:var(--muted)}
.reviewer{position:absolute;top:500px;display:flex;align-items:center;gap:10px}
.avatar{width:42px;height:42px;border-radius:50%;background:linear-gradient(135deg,#c7b3a0,#5f5448)}
.reviewer b{display:block;font-weight:400;font-size:17px;color:var(--brown);line-height:20px}
.reviewer small{font-size:10.5px;color:#333}

.cta{top:3299px;height:362px;background:var(--band)}
.cta-title{left:94px;top:98px;font-family:"Ubuntu",sans-serif;font-weight:500;font-size:46px;line-height:61px;color:var(--white);letter-spacing:1px;white-space:nowrap}
.cta-text{left:96px;top:222px;width:620px;font-size:12.5px;line-height:22px;color:#f3ece5}
.cta-divider{left:790px;top:92px;width:2px;height:174px;background:var(--white)}
.cta-phone{left:935px;top:126px;width:171px;height:47px;border:2px solid var(--white);border-radius:4px;color:var(--white);font-size:14px;display:flex;align-items:center;justify-content:center;gap:10px}
.cta-contact{left:935px;top:194px;width:171px;height:45px;background:var(--white);border-radius:4px;color:var(--brown);font-size:13px;display:flex;align-items:center;justify-content:center}

.contact{top:3661px;height:552px}
.contact-panel{left:0;top:0;width:618px;height:552px;background:var(--beige)}
.contact-photo{left:618px;top:0;width:582px;height:552px;background:linear-gradient(110deg,#cbb9a3 0%,#6f7a5e 45%,#4f5a48 70%,#a9ab8c 100%)}
.field{position:absolute;height:35px;background:var(--white);font-size:11px;color:#888;padding:10px 16px}
.send-btn{left:134px;top:445px;width:418px;height:35px;font-size:11.5px}

.site-footer{top:4213px;height:379px;background:var(--band);color:var(--white)}
.foot-head{font-size:15px;font-weight:600;letter-spacing:.3px}
.foot-item{position:absolute;left:93px;display:flex;gap:16px;font-size:11px;line-height:22px}
.foot-brand{left:0;width:1200px;top:92px;font-family:"Ubuntu",sans-serif;font-weight:500;font-size:28px;display:flex;justify-content:center;align-items:center;gap:10px}
.foot-brand .brand-dot{background:var(--white)}
.foot-text{left:455px;top:165px;width:290px;text-align:center;font-size:11px;line-height:21px}
.social{position:absolute;top:249px;width:36px;height:36px;border:1px solid var(--white);display:flex;align-items:center;justify-content:center}
.social i{width:9px;height:9px;border-radius:50%;background:var(--white)}
.hours{position:absolute;right:94px;display:flex;align-items:center;gap:14px;font-size:11px}
.foot-rule{left:62px;top:330px;width:1076px;height:1px;background:#e7dccf}
.copyright{left:0;top:347px;width:1200px;text-align:center;font-size:11px}
</style>
</head>
<body>

<div class="top-bar">
  <svg width="12" height="14" viewBox="0 0 12 14"><path d="M6 1a4.5 4.5 0 0 0-4.5 4.5C1.5 9 6 13 6 13s4.5-4 4.5-7.5A4.5 4.5 0 0 0 6 1z" fill="none" stroke="#fff" stroke-width="1.3"/><circle cx="6" cy="5.5" r="1.6" fill="#fff"/></svg>
  6015 Some place somewhere
</div>

<header class="site-header">
  <div class="abs brand"><span class="brand-dot"></span>Willowmere Group</div>
  <div class="abs header-phone">
    <svg width="16" height="16" viewBox="0 0 24 24"><path d="M6.6 10.8a15 15 0 0 0 6.6 6.6l2.2-2.2a1 1 0 0 1 1-.25 11.4 11.4 0 0 0 3.6.57 1 1 0 0 1 1 1V20a1 1 0 0 1-1 1A17 17 0 0 1 3 4a1 1 0 0 1 1-1h3.5a1 1 0 0 1 1 1c0 1.25.2 2.45.57 3.57a1 1 0 0 1-.25 1z" fill="#9e8164"/></svg>
    (000) 123-4567
  </div>
  <div class="abs btn header-cta">REQUEST APPOINTMENT</div>
  <nav class="abs main-nav">
    <span class="active">HOME</span><span>ABOUT US</span><span>CONDITIONS</span><span>TREATMENTS</span><span>GALLERY</span><span>DOCTORS</span><span>CONTACT US</span>
  </nav>
</header>

<section class="hero">
  <div class="photo hero-photo" role="img" aria-label="Therapist holding up emotion cards to a client"></div>
  <div class="abs hero-tag">Therapy Experts</div>
  <h1 class="abs hero-title">Unlock Your True<br>Potential, Find<br>Inner Peace</h1>
  <p class="abs hero-text">Lorem ipsum dolor sit amet, consectetur adipiscing elit, sed do eiusmod tempor incididunt ut labore et dolore magna</p>
  <div class="abs btn hero-btn">Discover more</div>
</section>

<section class="conditions">
  <div class="abs eyebrow" style="left:97px;top:92px">Our Treatments</div>
  <h2 class="abs heading" style="left:94px;top:125px;font-size:46px">Conditions We Treat</h2>
  <div class="arrow-btn" style="left:1005px;top:108px"><svg width="10" height="16" viewBox="0 0 10 16"><path d="M8 2 2 8l6 6" fill="none" stroke="#222" stroke-width="1.6"/></svg></div>
  <div class="arrow-btn" style="left:1060px;top:108px"><svg width="10" height="16" viewBox="0 0 10 16"><path d="m2 2 6 6-6 6" fill="none" stroke="#222" stroke-width="1.6"/></svg></div>

  <article class="card" style="left:90px">
    <div class="photo" style="background:linear-gradient(120deg,#d9cfc4,#b79e85 60%,#6d5a48)" role="img" aria-label="Teenager talking with a counsellor"></div>
    <div class="card-icon"><svg width="28" height="28" viewBox="0 0 24 24"><path d="M12 3l2.6 5.3 5.8.8-4.2 4.1 1 5.8L12 16.3 6.8 19l1-5.8L3.6 9.1l5.8-.8z" fill="none" stroke="#fff" stroke-width="1.5"/></svg></div>
    <h3>Addictions</h3>
    <p>Lorem ipsum dolor sit amet, consectetur adi piscing elit sed do eiusmod tmpor</p>
    <span class="rule"></span>
  </article>
  <article class="card" style="left:439px">
    <div class="photo" style="background:linear-gradient(120deg,#e4e1dc,#b9ab9a 55%,#5c5651)" role="img" aria-label="Client speaking with a therapist taking notes"></div>
    <div class="card-icon"><svg width="28" height="28" viewBox="0 0 24 24"><path d="M12 20.5 4.2 12.8A4.8 4.8 0 0 1 11 6l1 1 1-1a4.8 4.8 0 0 1 6.8 6.8z" fill="none" stroke="#fff" stroke-width="1.5" stroke-linejoin="round"/><path d="M12 7l-1.5 4 3 2-1.5 4" fill="none" stroke="#fff" stroke-width="1.5" stroke-linejoin="round"/></svg></div>
    <h3>Betrayal Trauma</h3>
    <p>Lorem ipsum dolor sit amet, consectetur adi piscing elit sed do eiusmod tmpor</p>
    <span class="rule"></span>
  </article>
  <article class="card" style="left:787px">
    <div class="photo" style="background:linear-gradient(120deg,#c99a7a,#e3ddd5 50%,#c8c3bd)" role="img" aria-label="Client in a counselling session gesturing while talking"></div>
    <div class="card-icon"><svg width="28" height="28" viewBox="0 0 24 24"><path d="M8 13V5.5a1.3 1.3 0 0 1 2.6 0V11m0-6.5a1.3 1.3 0 0 1 2.6 0V11m0-5a1.3 1.3 0 0 1 2.6 0v5.5m0-3a1.3 1.3 0 0 1 2.6 0V15a6 6 0 0 1-6 6h-.5A6 6 0 0 1 6 17l-2-3.5a1.3 1.3 0 0 1 2.2-1.3L8 14" fill="none" stroke="#fff" stroke-width="1.4"/></svg></div>
    <h3>EMDR</h3>
    <p>Lorem ipsum dolor sit amet, consectetur adi piscing elit sed do eiusmod tmpor</p>
    <span class="rule"></span>
  </article>
</section>

<section class="why">
  <div class="abs eyebrow" style="left:97px;top:82px">Treatments</div>
  <h2 class="abs heading" style="left:94px;top:112px;font-size:44px;line-height:60px">Why Choose<br>Willowmere</h2>
  <p class="abs body-text" style="left:97px;top:244px;width:440px">Lorem ipsum dolor sit amet, consectetur adipiscing elit, sed do eiusmo empor incididunt ut abore et dolore magna aliqua. Ut enim ad minim iam, quis nostrud exercitation ullamco</p>

  <div class="feature" style="left:103px;top:350px;height:80px">
    <svg width="32" height="32" viewBox="0 0 32 32"><path d="M4 28h24M8 28l4-10 6-4 4 6-6 4M12 18l3-9 5 1" fill="none" stroke="#9e8164" stroke-width="1.5"/></svg>
    <h4>Results-Oriented</h4><p>Lorem ipsum dolor sit amet, consectetur adipiscing</p>
  </div>
  <div class="feature" style="left:403px;top:350px;height:80px">
    <svg width="32" height="32" viewBox="0 0 32 32"><circle cx="16" cy="16" r="11" fill="none" stroke="#9e8164" stroke-width="1.5"/><path d="M16 10v6l4 3M5 10l2 3 3-2" fill="none" stroke="#9e8164" stroke-width="1.5"/></svg>
    <h4>Long-Term Support</h4><p>Lorem ipsum dolor sit amet, consectetur adipiscing</p>
  </div>
  <div class="feature" style="left:103px;top:446px;height:80px">
    <svg width="32" height="32" viewBox="0 0 32 32"><circle cx="16" cy="11" r="6" fill="none" stroke="#9e8164" stroke-width="1.5"/><path d="M5 28a11 8 0 0 1 22 0z" fill="none" stroke="#9e8164" stroke-width="1.5"/></svg>
    <h4>Client-Centered</h4><p>Lorem ipsum dolor sit amet, consectetur adipiscing</p>
  </div>
  <div class="feature" style="left:403px;top:446px;height:80px">
    <svg width="32" height="32" viewBox="0 0 32 32"><path d="M16 4l3.5 7.3 8 1.1-5.8 5.6 1.4 7.9L16 22.2l-7.1 3.7 1.4-7.9L4.5 12.4l8-1.1z" fill="none" stroke="#9e8164" stroke-width="1.5"/></svg>
    <h4>Convenient Location</h4><p>Lorem ipsum dolor sit amet, consectetur adipiscing</p>
  </div>

  <div class="abs btn" style="left:103px;top:561px;width:155px;height:44px;font-size:14px;gap:14px">Contact us
    <svg width="18" height="12" viewBox="0 0 18 12"><path d="M1 6h15M11 1l5 5-5 5" fill="none" stroke="#fff" stroke-width="1.5"/></svg>
  </div>

  <div class="abs ring"></div>
  <div class="abs ring-photo" role="img" aria-label="Therapist in a session with a client"></div>
</section>

<section class="about">
  <div class="abs about-panel"></div>
  <div class="abs about-frame" role="img" aria-label="Family sitting on a sofa with a counsellor"></div>
  <div class="abs eyebrow" style="left:648px;top:86px">About Us</div>
  <h2 class="abs heading" style="left:646px;top:117px;font-size:46px;line-height:61px">Healing Minds,<br>Restoring Hearts</h2>
  <p class="abs body-text" style="left:648px;top:250px;width:460px">Lorem ipsum dolor sit amet, consectetur adipiscing elit, sed do eiusmo empor incididunt ut abore et dolore magna aliqua. Ut enim ad minim iam, quis nostrud exercitation ullamco</p>
  <div class="abs btn" style="left:648px;top:355px;width:169px;height:47px;font-size:13px">Apply Now</div>
</section>

<section class="testimonials">
  <div class="abs eyebrow" style="left:92px;top:80px">Testimonials</div>
  <h2 class="abs heading" style="left:90px;top:114px;font-size:46px">What Clients Are Saying</h2>
  <div class="arrow-btn" style="left:1002px;top:96px"><svg width="10" height="16" viewBox="0 0 10 16"><path d="M8 2 2 8l6 6" fill="none" stroke="#222" stroke-width="1.6"/></svg></div>
  <div class="arrow-btn" style="left:1055px;top:96px"><svg width="10" height="16" viewBox="0 0 10 16"><path d="m2 2 6 6-6 6" fill="none" stroke="#222" stroke-width="1.6"/></svg></div>

  <div class="quote-card" style="left:90px">
    <svg class="quote-mark" width="50" height="36" viewBox="0 0 50 36"><path d="M2 36V16Q2 2 18 0v7Q10 9 10 16h10v20zM28 36V16Q28 2 44 0v7Q36 9 36 16h10v20z" fill="#9e8164"/></svg>
    <div class="stars">★★★★★</div><h4>They are the Best</h4>
    <p>Lorem ipsum dolor sit amet, consectetur adipiscing elit, sed do eiusmod tempor incididunt ut labore et dolore magna aliqua. Ut enim ad minim veniam, quis nostrud exercitation ullamco laboris nisi ut</p>
  </div>
  <div class="quote-card" style="left:437px">
    <svg class="quote-mark" width="50" height="36" viewBox="0 0 50 36"><path d="M2 36V16Q2 2 18 0v7Q10 9 10 16h10v20zM28 36V16Q28 2 44 0v7Q36 9 36 16h10v20z" fill="#9e8164"/></svg>
    <div class="stars">★★★★★</div><h4>They are the Best</h4>
    <p>Lorem ipsum dolor sit amet, consectetur adipiscing elit, sed do eiusmod tempor incididunt ut labore et dolore magna aliqua. Ut enim ad minim veniam, quis nostrud exercitation ullamco laboris nisi ut</p>
  </div>
  <div class="quote-card" style="left:783px">
    <svg class="quote-mark" width="50" height="36" viewBox="0 0 50 36"><path d="M2 36V16Q2 2 18 0v7Q10 9 10 16h10v20zM28 36V16Q28 2 44 0v7Q36 9 36 16h10v20z" fill="#9e8164"/></svg>
    <div class="stars">★★★★★</div><h4>They are the Best</h4>
    <p>Lorem ipsum dolor sit amet, consectetur adipiscing elit, sed do eiusmod tempor incididunt ut labore et dolore magna aliqua. Ut enim ad minim veniam, quis nostrud exercitation ullamco laboris nisi ut</p>
  </div>

  <div class="reviewer" style="left:122px"><div class="avatar" role="img" aria-label="Client portrait"></div><div><b>Elena</b><small>CEO, Fernwood Co</small></div></div>
  <div class="reviewer" style="left:469px"><div class="avatar" role="img" aria-label="Client portrait"></div><div><b>Elena</b><small>CEO, Fernwood Co</small></div></div>
  <div class="reviewer" style="left:815px"><div class="avatar" role="img" aria-label="Client portrait"></div><div><b>Elena</b><small>CEO, Fernwood Co</small></div></div>
</section>

<section class="cta">
  <h2 class="abs cta-title">Get in touch with us for<br>expert therapy solutions</h2>
  <p class="abs cta-text">Lorem ipsum dolor sit amet, consectetur adipiscing elit, sed do eiusmoempor incididunt ut abore et dolore magna aliqua. Ut enim ad minim iam</p>
  <div class="abs cta-divider"></div>
  <div class="abs cta-phone">
    <svg width="15" height="15" viewBox="0 0 24 24"><path d="M6.6 10.8a15 15 0 0 0 6.6 6.6l2.2-2.2a1 1 0 0 1 1-.25 11.4 11.4 0 0 0 3.6.57 1 1 0 0 1 1 1V20a1 1 0 0 1-1 1A17 17 0 0 1 3 4a1 1 0 0 1 1-1h3.5a1 1 0 0 1 1 1c0 1.25.2 2.45.57 3.57a1 1 0 0 1-.25 1z" fill="#fff"/></svg>
    +123 456 789
  </div>
  <div class="abs cta-contact">Contact Us</div>
</section>

<section class="contact">
  <div class="abs contact-panel"></div>
  <div class="abs contact-photo" role="img" aria-label="Client talking with a therapist holding a clipboard"></div>
  <div class="abs eyebrow" style="left:135px;top:76px">Get in Touch</div>
  <h2 class="abs heading" style="left:133px;top:108px;font-size:46px">Contact Us</h2>
  <p class="abs" style="left:138px;top:175px;font-size:11px;color:var(--muted)">Just send a message, we will answer within 24 hours</p>
  <div class="field" style="left:134px;top:233px;width:199px">Your full name</div>
  <div class="field" style="left:353px;top:233px;width:199px">Phone Number</div>
  <div class="field" style="left:134px;top:284px;width:199px">Mail Address</div>
  <div class="field" style="left:353px;top:284px;width:199px">Subject</div>
  <div class="field" style="left:134px;top:334px;width:418px;height:87px">Type your message...</div>
  <div class="abs btn send-btn">Send Your Message</div>
</section>

<footer class="site-footer">
  <div class="abs foot-head" style="left:93px;top:117px">CONTACT US</div>
  <div class="foot-item" style="top:158px">
    <svg width="14" height="18" viewBox="0 0 12 14"><path d="M6 1a4.5 4.5 0 0 0-4.5 4.5C1.5 9 6 13 6 13s4.5-4 4.5-7.5A4.5 4.5 0 0 0 6 1z" fill="#fff"/><circle cx="6" cy="5.5" r="1.6" fill="#a68a6d"/></svg>
    <span>101- lorem ipsum simple text<br>print type text industry text.</span>
  </div>
  <div class="foot-item" style="top:215px">
    <svg width="14" height="14" viewBox="0 0 24 24"><path d="M6.6 10.8a15 15 0 0 0 6.6 6.6l2.2-2.2a1 1 0 0 1 1-.25 11.4 11.4 0 0 0 3.6.57 1 1 0 0 1 1 1V20a1 1 0 0 1-1 1A17 17 0 0 1 3 4a1 1 0 0 1 1-1h3.5a1 1 0 0 1 1 1c0 1.25.2 2.45.57 3.57a1 1 0 0 1-.25 1z" fill="#fff"/></svg>
    <span>123 456 7890</span>
  </div>
  <div class="foot-item" style="top:250px">
    <svg width="15" height="12" viewBox="0 0 16 12"><rect x="0.5" y="0.5" width="15" height="11" fill="#fff"/><path d="M1 1l7 6 7-6" fill="none" stroke="#a68a6d" stroke-width="1.2"/></svg>
    <span>hello@willowmere.example</span>
  </div>

  <div class="abs foot-brand"><span class="brand-dot"></span>Willowmere Group</div>
  <p class="abs foot-text">Lorem ipsum dolor sit amet, consectetur adipisc ing elit, sed do eiusmod tempor incididunt sed ut labore et dolore magna</p>
  <div class="social" style="left:537px"><i></i></div>
  <div class="social" style="left:582px"><i></i></div>
  <div class="social" style="left:627px"><i></i></div>

  <div class="abs foot-head" style="right:94px;top:117px">OPENING HOURS</div>
  <div class="hours" style="top:166px">Mon - Fri: 9am - to - 6pm <svg width="14" height="14" viewBox="0 0 14 14"><circle cx="7" cy="7" r="6" fill="none" stroke="#fff"/><path d="M7 3.5V7l2.5 1.5" fill="none" stroke="#fff"/></svg></div>
  <div class="hours" style="top:197px">Saturday 9am - to - 2pm <svg width="14" height="14" viewBox="0 0 14 14"><circle cx="7" cy="7" r="6" fill="none" stroke="#fff"/><path d="M7 3.5V7l2.5 1.5" fill="none" stroke="#fff"/></svg></div>
  <div class="hours" style="top:227px"><span>Sunday : <u>Closed</u></span> <svg width="14" height="14" viewBox="0 0 14 14"><circle cx="7" cy="7" r="6" fill="none" stroke="#fff"/><path d="M7 3.5V7l2.5 1.5" fill="none" stroke="#fff"/></svg></div>

  <div class="abs foot-rule"></div>
  <div class="abs copyright">All Rights Reserved, 2023</div>
</footer>

</body>
</html>
```